KV HOLDING Business Cards

I need business cards for "KV Holding group LLC" doublesided... logo on the back (also include logo on front)
logo attached to project... i have jpg up..
Company Info:
418 East Marlow Avenue, Suite 7B
Chicago, Illinois 60617
facsimile 312-555-0188 (list fax, address, website on all cards.)
www.kvholdinggroup.example
Three different people on cards:
Dorian P. Kell, CPA MST
Principal
ofc 312-555-0142
mobile 312-555-0167
dorianpkell@kvholdinggroup.example
Marcus T. Brenholt, CPA MST
Principal
marcustbrenholt@kvholdinggroup.example
mobile 708-555-0119
ofc 312-555-0142
Nigel F Carrow
Principal
ofc 312-555-0142
no mobile
nigelfcarrow@kvholdinggroup.example
I have multiple projects listed.. see below:
Business cards for amber gate equity llc
letterhead
envelopes
Business cards for KV Holding LLC
letterhead
envelopes
Target Market(s)
rich people
Industry/Entity Type
Business
Look and feel

```html
<!DOCTYPE html>
<html lang="en">
<head>
<meta charset="utf-8">
<title>KV Holding Group LLC — Business Cards</title>
<link href="https://fonts.googleapis.com/css2?family=Cinzel:wght@500&family=Tinos:ital,wght@0,400;0,700;1,400&display=swap" rel="stylesheet">
<style>
  :root {
    --backdrop: #e6e6e6;
    --navy: #174577;
    --navy-soft: #2f5e93;
    --paper: #ffffff;
    --silver: #e4e6ea;
    --silver-muted: #c3c9d3;
    --ink: #111111;
    --grey-text: #4a4a4a;
    --label-blue: #b9c7da;
    --mark-tint: #3a6aa0;
  }
  * { margin: 0; padding: 0; box-sizing: border-box; }
  html, body {
    width: 1200px; height: 1000px; overflow: hidden;
    background: var(--backdrop);
  }
  .canvas { position: relative; width: 1200px; height: 1000px; }

  .card {
    position: absolute;
    overflow: hidden;
    box-shadow: 3px 4px 6px rgba(0,0,0,0.35);
  }
  .card--front {
    left: 249px; top: 24px; width: 702px; height: 454px;
    background: var(--navy);
  }
  .card--back {
    left: 253px; top: 520px; width: 695px; height: 455px;
    background: var(--paper);
  }

  .brand-mark {
    position: absolute; left: 50%;
    border-radius: 50%;
    transform: translateX(-50%);
  }
  .card--front .brand-mark {
    top: 70px; width: 150px; height: 150px;
    background: var(--mark-tint);
  }
  .card--back .brand-mark {
    top: 40px; width: 110px; height: 110px;
    background: var(--navy);
  }

  .brand-name {
    position: absolute; left: 0; right: 0;
    text-align: center;
    font-family: "Cinzel", serif;
    font-weight: 500;
    white-space: nowrap;
  }
  .card--front .brand-name {
    top: 248px; font-size: 38px; color: var(--silver);
  }
  .card--back .brand-name {
    top: 160px; font-size: 28px; color: var(--navy);
  }

  .person-name {
    position: absolute; left: 0; right: 0; top: 322px;
    text-align: center;
    font-family: "Tinos", serif;
    font-size: 31px; color: var(--silver);
  }
  .person-title {
    position: absolute; left: 0; right: 0; top: 364px;
    text-align: center;
    font-family: "Tinos", serif; font-style: italic;
    font-size: 24px; color: var(--silver-muted);
  }

  .address {
    position: absolute; left: 0; right: 0; top: 208px;
    text-align: center;
    font-family: "Tinos", serif;
    font-size: 20px; color: var(--grey-text);
  }
  .website {
    position: absolute; left: 0; right: 0; top: 238px;
    text-align: center;
    font-family: "Tinos", serif; font-weight: 700;
    font-size: 21px; color: var(--ink);
  }

  .contact-band {
    position: absolute; left: 0; right: 0; top: 288px; bottom: 0;
    background: var(--navy);
    font-family: "Tinos", serif;
    color: var(--paper);
    text-align: center;
  }
  .contact-line {
    position: absolute; left: 0; right: 0;
    font-size: 23px; white-space: nowrap;
  }
  .contact-line--phones { top: 55px; }
  .contact-line--email { top: 88px; font-size: 22px; }
  .label { font-weight: 700; color: var(--label-blue); }
  .divider { color: var(--label-blue); margin: 0 14px; }
</style>
</head>
<body>
<main class="canvas">

  <section class="card card--front" aria-label="Business card front">
    <div class="brand-mark" aria-hidden="true"></div>
    <div class="brand-name">KV Holding Group LLC</div>
    <div class="person-name">Dorian P. Kell, CPA MST</div>
    <div class="person-title">Principal</div>
  </section>

  <section class="card card--back" aria-label="Business card back">
    <div class="brand-mark" aria-hidden="true"></div>
    <div class="brand-name">KV Holding Group LLC</div>
    <div class="address">418 East Marlow Avenue, Suite 7B, Chicago, Illinois 60617</div>
    <div class="website">www.kvholdinggroup.example</div>
    <div class="contact-band">
      <div class="contact-line contact-line--phones">
        <span class="label">T:</span> 312-555-0142<span class="divider">|</span><span class="label">M:</span> 312-555-0167<span class="divider">|</span><span class="label">F:</span> 312-555-0188
      </div>
      <div class="contact-line contact-line--email">
        <span class="label">E:</span> dorianpkell@kvholdinggroup.example
      </div>
    </div>
  </section>

</main>
</body>
</html>
```